New modern business card design

To design a brand new business card that's clean & modern in terms of layout.
I have attached our company logo and also basic information regarding what is needed on the card that also needs to be editable.

Target Market(s)

motor trade

Contact Information for Business Card

logo, name, title, tel, mob, email, address, www, all information is in the word.doc file

Requirements
Must have
• white background
Nice to have
• Nice clean font

```html
<!DOCTYPE html>
<html lang="en">
<head>
<meta charset="utf-8">
<title>Boltway Ltd – Business Card</title>
<link rel="stylesheet" href="https://fonts.googleapis.com/css2?family=Montserrat:wght@400;500;600&display=swap">
<style>
  :root {
    --bg: #2b2b2b;
    --card: #ffffff;
    --blue: #1f6aad;
    --blue-deep: #185a96;
    --grey: #b9bcc0;
    --ink-light: #ffffff;
    --shadow: rgba(0,0,0,0.45);
  }
  * { margin: 0; padding: 0; box-sizing: border-box; }
  html, body {
    width: 1200px; height: 997px; overflow: hidden;
    background: var(--bg);
    font-family: "Montserrat", Arial, sans-serif;
  }
  .stage { position: relative; width: 1200px; height: 997px; }
  .card {
    position: absolute; width: 540px; height: 350px;
    background: var(--card); overflow: hidden;
    box-shadow: 0 14px 34px var(--shadow);
  }
  .card--contact { left: 40px; top: 230px; }
  .card--offer { left: 620px; top: 417px; }
  .card__wave { position: absolute; inset: 0; width: 100%; height: 100%; }

  .brand {
    position: absolute; display: flex; flex-direction: column; align-items: center;
  }
  .brand__row { display: flex; align-items: center; gap: 10px; }
  .brand__mark { width: 22px; height: 22px; background: var(--blue); }
  .brand__name {
    color: var(--blue); font-weight: 600; font-size: 30px; letter-spacing: 2px;
  }
  .brand__rule { width: 260px; height: 1.5px; background: var(--blue); margin-top: 8px; }
  .card--contact .brand { left: 210px; top: 64px; }
  .card--contact .brand__name { font-size: 26px; }
  .card--contact .brand__rule { width: 230px; }
  .card--offer .brand { left: 130px; top: 70px; }

  .person {
    position: absolute; left: 34px; top: 238px; color: var(--ink-light);
  }
  .person__name { font-size: 15px; font-weight: 500; letter-spacing: 1px; }
  .person__title { font-size: 11px; margin-top: 1px; }
  .person__lines { margin-top: 12px; font-size: 11px; line-height: 1.45; }
  .contact-line { display: flex; align-items: flex-start; gap: 8px; }
  .contact-line__icon {
    width: 11px; height: 11px; margin-top: 2px; border-radius: 50%;
    background: var(--ink-light); flex: none;
  }
  .web {
    position: absolute; right: 24px; bottom: 28px;
    color: var(--ink-light); font-size: 11px; font-weight: 500;
  }

  .offer {
    position: absolute; left: 40px; top: 238px; color: var(--ink-light);
    display: flex; align-items: center; gap: 14px;
  }
  .offer__icon { width: 44px; height: 44px; flex: none; }
  .offer__headline { font-size: 15px; font-weight: 500; letter-spacing: 2.5px; }
  .offer__numbers {
    display: flex; gap: 36px; margin-top: 6px;
    font-size: 19px; font-weight: 500; letter-spacing: 1px;
  }
</style>
</head>
<body>
<main class="stage">

  <section class="card card--contact" aria-label="Business card, contact side">
    <svg class="card__wave" viewBox="0 0 540 350" preserveAspectRatio="none" aria-hidden="true">
      <path d="M0 205 C150 165 330 175 540 95 L540 110 C330 192 150 182 0 222 Z" fill="var(--grey)"/>
      <path d="M0 226 C150 186 330 196 540 114 L540 350 L0 350 Z" fill="var(--blue)"/>
      <path d="M230 188 C380 180 480 135 540 70" fill="none" stroke="var(--grey)" stroke-width="5"/>
    </svg>
    <div class="brand">
      <div class="brand__row">
        <span class="brand__mark"></span>
        <span class="brand__name">BOLTWAY LTD</span>
      </div>
      <div class="brand__rule"></div>
    </div>
    <div class="person">
      <p class="person__name">DANIEL MARSH</p>
      <p class="person__title">General Manager</p>
      <div class="person__lines">
        <p class="contact-line"><span class="contact-line__icon"></span>dmarsh@boltway-ltd.co.uk</p>
        <p class="contact-line"><span class="contact-line__icon"></span>Kestrel Road Denbury<br>Northfield NF2 7QA</p>
      </div>
    </div>
    <p class="web">www.boltway-ltd.co.uk</p>
  </section>

  <section class="card card--offer" aria-label="Business card, quote side">
    <svg class="card__wave" viewBox="0 0 540 350" preserveAspectRatio="none" aria-hidden="true">
      <path d="M0 205 C150 165 330 175 540 95 L540 110 C330 192 150 182 0 222 Z" fill="var(--grey)"/>
      <path d="M0 226 C150 186 330 196 540 114 L540 350 L0 350 Z" fill="var(--blue)"/>
      <path d="M230 188 C380 180 480 135 540 70" fill="none" stroke="var(--grey)" stroke-width="5"/>
    </svg>
    <div class="brand">
      <div class="brand__row">
        <span class="brand__mark"></span>
        <span class="brand__name">BOLTWAY LTD</span>
      </div>
      <div class="brand__rule"></div>
    </div>
    <div class="offer">
      <svg class="offer__icon" viewBox="0 0 44 44" aria-hidden="true">
        <path d="M22 3 A19 19 0 1 1 9 36 L4 41 L6 32 A19 19 0 0 1 22 3 Z" fill="var(--ink-light)"/>
        <path d="M16 13 l4 0 l2 6 l-3 2 a12 12 0 0 0 5 5 l2 -3 l6 2 l0 4 a3 3 0 0 1 -3 3 a18 18 0 0 1 -16 -16 a3 3 0 0 1 3 -3 Z" fill="var(--blue)"/>
      </svg>
      <div>
        <p class="offer__headline">CALL FOR A FREE NO OBLIGATION QUOTE</p>
        <p class="offer__numbers"><span>0140 555 0182</span><span>07700 900 415</span></p>
      </div>
    </div>
  </section>

</main>
</body>
</html>
```